Etiketten für Getränkedose (0,2 L)
Zielgruppe
Verkauf von Summerdrinks (Getränkedosen), stylisher Summerdrink (leicht alkoholhältig auf Rotwein basierend)
Aufgabenstellung
ich möchte eine Getränkedose (0,2 Liter wie Energydrink, etc.) designen lassen. Motiv ist etwas sommerliches, der Name ist olaGiardino welcher auf der Dose sein soll. Außerdem soll es vlt Paisley Muster und rote und gelbe Farbtöne enthalten (Giardino). Evtl. ein Bezug zu LGBT (rainbow logo) auch enthalten sein...
https://www.bildkammerfeld.de/de/search/paisley+rot hier meine Inspiration, kann aber auch etwas anders sein...

```html
<!DOCTYPE html>
<html lang="de">
<head>
<meta charset="utf-8">
<title>olaGiardino Tinto – Dosenetikett</title>
<link rel="stylesheet" href="https://fonts.googleapis.com/css2?family=Josefin+Sans:wght@300;400&family=Shrikhand&display=swap">
<style>
  :root {
    --backdrop: #ff2479;
    --white: #ffffff;
    --berry: #c8145a;
    --berry-light: #de5a86;
    --leaf: #5cc86a;
    --leaf-deep: #3fae5c;
    --amber: #d6a05a;
    --plum: #a8357a;
    --mint: #7ff0d0;
    --blush: #f6c4d6;
  }
  html, body {
    margin: 0;
    padding: 0;
    width: 1200px;
    height: 1200px;
    overflow: hidden;
    background: var(--backdrop);
  }
  .canvas {
    position: relative;
    width: 1200px;
    height: 1200px;
    background: var(--backdrop);
  }
  .can-label {
    position: absolute;
    left: 335px;
    top: 239px;
    width: 290px;
    height: 680px;
  }
  .brand-lockup {
    position: absolute;
    left: 640px;
    top: 300px;
    width: 540px;
    text-align: right;
    color: var(--white);
    font-family: "Josefin Sans", sans-serif;
  }
  .brand-lockup .brand-name {
    display: block;
    font-weight: 400;
    font-size: 100px;
    line-height: 1;
    letter-spacing: -1px;
  }
  .brand-lockup .variety {
    display: block;
    margin-top: 22px;
    margin-right: 96px;
    font-weight: 300;
    font-size: 60px;
    letter-spacing: 4px;
    line-height: 1;
  }
  .label-brand {
    font-family: "Josefin Sans", sans-serif;
  }
  .label-holiday {
    font-family: "Shrikhand", cursive;
  }
</style>
</head>
<body>
<main class="canvas">
  <svg class="can-label" viewBox="0 0 290 680" xmlns="http://www.w3.org/2000/svg">
    <defs>
      <clipPath id="label-clip">
        <rect x="0" y="0" width="290" height="680"/>
      </clipPath>
      <linearGradient id="pattern-upper" x1="0" y1="0" x2="1" y2="0.3">
        <stop offset="0" stop-color="var(--leaf)"/>
        <stop offset="0.25" stop-color="var(--amber)"/>
        <stop offset="0.5" stop-color="var(--leaf-deep)"/>
        <stop offset="0.75" stop-color="var(--amber)"/>
        <stop offset="1" stop-color="var(--leaf)"/>
      </linearGradient>
      <linearGradient id="pattern-lower" x1="0" y1="0" x2="1" y2="1">
        <stop offset="0" stop-color="var(--plum)"/>
        <stop offset="0.35" stop-color="var(--leaf)"/>
        <stop offset="0.6" stop-color="var(--amber)"/>
        <stop offset="0.85" stop-color="var(--plum)"/>
        <stop offset="1" stop-color="var(--amber)"/>
      </linearGradient>
      <linearGradient id="badge-fill" x1="0" y1="0" x2="1" y2="0">
        <stop offset="0" stop-color="var(--berry-light)"/>
        <stop offset="0.55" stop-color="var(--berry)"/>
        <stop offset="1" stop-color="var(--berry)"/>
      </linearGradient>
      <linearGradient id="holiday-fill" x1="0" y1="1" x2="1" y2="0">
        <stop offset="0" stop-color="var(--mint)"/>
        <stop offset="0.5" stop-color="var(--blush)"/>
        <stop offset="1" stop-color="var(--mint)"/>
      </linearGradient>
    </defs>
    <g clip-path="url(#label-clip)">
      <rect class="pattern-band pattern-band--upper" x="0" y="0" width="290" height="276" fill="url(#pattern-upper)" role="img" aria-label="Paisley-Muster in Grün- und Orangetönen"/>
      <rect class="pattern-band pattern-band--lower" x="0" y="276" width="290" height="404" fill="url(#pattern-lower)" role="img" aria-label="Paisley-Muster in Magenta-, Orange- und Grüntönen"/>
      <circle class="brand-badge" cx="146" cy="294" r="110" fill="url(#badge-fill)"/>
      <text class="label-brand" x="146" y="316" text-anchor="middle" font-size="37" font-weight="400" fill="var(--white)">olaGiardino</text>
      <text class="label-brand" x="173" y="366" text-anchor="middle" font-size="24" font-weight="300" letter-spacing="2" fill="var(--white)">TINTO</text>
      <text class="label-holiday" transform="translate(22 690) rotate(-44)" font-size="104" textLength="372" lengthAdjust="spacingAndGlyphs" fill="url(#holiday-fill)">Holiday</text>
    </g>
  </svg>

  <div class="brand-lockup">
    <span class="brand-name">olaGiardino</span>
    <span class="variety">TINTO</span>
  </div>
</main>
</body>
</html>
```